Female Focused - Finance Company needs a website

I need a website for a new company based in London called 'Marguerite Halloway Associates'. The company has been set up with a focus on empowering creativity and encouraging women to engage with finance and build their knowledge and understanding. I am targeting professional women and entrepreneurs in the late 20s to 40s age bracket. The mission is to empower women to achieve financial independence and inspire community and connectivity. I want to create a brand that promotes financial security, growth and connectivity.

The website at this stage can be relatively simple, I just want to be able to have a section about me and the work that I do, have contact details for people to be able to get in touch and find out more.

I run a series of different events and want to have a page whereby I can showcase the events that I am running. They can also use links to click through and register for events. I also want to be able to put images up of previous events that I have run. Maybe having a calendar on the website of different things that are happening.

I am creating a membership club called Loop4Loop and I want to have a page whereby they can find out about the membership and the different options that are available.

I have attached the logo below so you can see the designs so far.

I also own the domain name margueritehallowayassociates.example

```html
<!DOCTYPE html>
<html lang="en">
<head>
<meta charset="utf-8">
<title>Marguerite Halloway Associates</title>
<link rel="stylesheet" href="https://fonts.googleapis.com/css2?family=Montserrat:wght@400;500;600&display=swap">
<style>
:root{
  --ink:#1a1a1a;
  --slate:#6f6f6f;
  --button:#5a5a5a;
  --mist:#f2f2f2;
  --white:#ffffff;
  --black:#000000;
}
*{box-sizing:border-box;margin:0;padding:0}
html,body{width:1200px;height:3222px;overflow:hidden;background:var(--white)}
body{font-family:'Montserrat',sans-serif;color:var(--ink);position:relative}
.abs{position:absolute}
.btn{position:absolute;background:var(--button);color:var(--white);font-size:13px;font-weight:500;display:flex;align-items:center;justify-content:center;gap:18px;letter-spacing:.3px;text-decoration:none}

/* header */
.site-header{position:absolute;left:0;top:0;width:1200px;height:133px;background:var(--white)}
.brand-badge{position:absolute;left:140px;top:26px;width:164px;height:164px;border-radius:50%;background:var(--white);z-index:3;display:flex;align-items:center;justify-content:center;text-align:center}
.brand-badge span{font-size:12px;font-weight:500;line-height:1.35;width:110px;color:var(--ink)}
.nav a{position:absolute;top:64px;font-size:13px;color:var(--ink);text-decoration:none;font-weight:500}
.nav svg{vertical-align:-3px;margin-right:4px}

/* hero */
.hero{position:absolute;top:133px;left:0;width:1200px;height:567px}
.hero-panel{position:absolute;left:0;top:0;width:556px;height:567px;background:var(--slate);color:var(--white)}
.hero-photo{position:absolute;left:556px;top:0;width:644px;height:567px;
  background:
    radial-gradient(ellipse 30% 45% at 20% 55%,rgba(40,40,40,.55),transparent 70%),
    radial-gradient(ellipse 25% 45% at 48% 75%,rgba(170,70,60,.55),transparent 70%),
    radial-gradient(ellipse 35% 55% at 82% 70%,rgba(240,120,125,.9),transparent 70%),
    radial-gradient(ellipse 22% 30% at 40% 35%,rgba(235,205,185,.8),transparent 70%),
    radial-gradient(ellipse 22% 30% at 70% 32%,rgba(180,120,95,.75),transparent 70%),
    linear-gradient(180deg,#3e6a2c 0%,#6f9447 40%,#8fae60 70%,#7d9a55 100%)}
.hero-kicker{left:128px;top:116px;font-size:17px}
.hero-title{left:128px;top:144px;font-size:55px;font-weight:600;line-height:65px;width:420px}
.hero-copy{left:128px;top:370px;font-size:17px;line-height:20px;width:310px}

/* about */
.about-mark{left:191px;top:857px;width:262px;height:262px;border:2px solid var(--ink);border-radius:50%;display:flex;align-items:center;justify-content:center;text-align:center}
.about-mark span{font-size:24px;font-weight:500;line-height:1.3;width:200px}
.about-tagline{left:155px;top:1181px;font-size:18px;letter-spacing:5.6px;color:#444}
.about-kicker{left:606px;top:809px;font-size:18px}
.about-name{left:606px;top:848px;font-size:27px;font-weight:600}
.about-copy{left:606px;top:907px;font-size:12.4px;line-height:24.2px;white-space:nowrap}

/* services */
.services{position:absolute;left:0;top:1294px;width:1200px;height:541px;background:var(--mist)}
.center{width:1200px;left:0;text-align:center}
.service-photo{width:130px;height:130px;border-radius:50%;
  background:
    radial-gradient(ellipse 28% 34% at 72% 42%,#3e8ee0 0%,#b8d3ee 60%,transparent 75%),
    radial-gradient(ellipse 24% 40% at 24% 58%,#d2c4b6,transparent 75%),
    linear-gradient(180deg,#e9e5df 0%,#b9ada0 60%,#8e7f71 100%)}
.service-title{font-size:21px;font-weight:600}
.service-copy{font-size:13.4px;line-height:17px;width:175px}

/* events */
.event-photo{width:265px;height:181px}
.event-date{position:absolute;left:20px;bottom:24px;background:var(--white);font-size:10px;padding:4px 10px}
.event-title{font-size:17.5px;font-weight:600}
.event-copy{font-size:13.6px;line-height:17px;width:240px}
.event-one{background:
  radial-gradient(ellipse 30% 40% at 25% 35%,rgba(60,50,70,.5),transparent 70%),
  radial-gradient(ellipse 35% 40% at 70% 70%,rgba(225,120,100,.7),transparent 70%),
  linear-gradient(135deg,#f6d6c6,#f2b8a3 50%,#ea947d)}
.event-two{background:
  radial-gradient(ellipse 25% 35% at 25% 40%,rgba(230,140,150,.8),transparent 70%),
  radial-gradient(ellipse 25% 35% at 60% 30%,rgba(245,215,190,.8),transparent 70%),
  radial-gradient(ellipse 30% 40% at 80% 75%,rgba(60,40,80,.7),transparent 70%),
  linear-gradient(135deg,#4f5aa8,#d98fc0 50%,#5e6fbf)}
.event-three{background:
  radial-gradient(ellipse 40% 30% at 50% 30%,rgba(240,230,240,.35),transparent 70%),
  linear-gradient(180deg,#2a2d66 0%,#7a3a8a 30%,#d2436b 55%,#f27d2f 80%,#f59a2a 100%)}

/* contact */
.contact{position:absolute;left:0;top:2415px;width:1200px;height:565px;background:var(--mist)}
.contact-item{left:128px;display:flex;gap:6px}
.contact-item svg{flex:none}
.contact-item p{font-size:13.6px;line-height:20px;padding-top:6px}
.field{position:absolute;left:585px;width:398px;background:var(--white);border:1px solid #444;font-size:13px;color:#888;padding:14px 13px;box-shadow:0 2px 2px rgba(0,0,0,.2)}

/* footer */
.site-footer{position:absolute;left:0;top:2980px;width:1200px;height:242px;background:var(--black);color:var(--white)}
.footer-links a{position:absolute;top:66px;font-size:13.6px;color:var(--white);text-decoration:none}
.socials{left:0;top:168px;width:1200px;display:flex;justify-content:center;gap:22px}
.socials span{font-size:14px;font-weight:500;display:flex;align-items:center;gap:7px}
.socials i{width:14px;height:14px;border-radius:50%;background:var(--white);display:inline-block}
</style>
</head>
<body>

<header class="site-header">
  <div class="brand-badge"><span>Marguerite Halloway Associates</span></div>
  <nav class="nav">
    <a href="#" style="left:488px">HOME</a>
    <a href="#" style="left:570px">ABOUT</a>
    <a href="#" style="left:659px">EVENT</a>
    <a href="#" style="left:748px"><svg width="18" height="18" viewBox="0 0 18 18" fill="none" stroke="#1a1a1a" stroke-width="1.5"><circle cx="9" cy="6" r="4"/><path d="M2 17c0-4 3-6 7-6s7 2 7 6z"/></svg>MEMBER ACCESS</a>
  </nav>
  <a class="btn" href="#" style="left:919px;top:47px;width:154px;height:47px">LET'S MEET</a>
</header>

<section class="hero">
  <div class="hero-panel">
    <p class="abs hero-kicker">Marguerite Halloway Associates</p>
    <h1 class="abs hero-title">Empowering Woman Creativity</h1>
    <p class="abs hero-copy">Lorem ipsum dolor sit amet consectetur. Facilisi ultrices neque dictum metus venenatis.</p>
  </div>
  <div class="hero-photo" role="img" aria-label="Photo of a group of smiling women together outdoors in a park"></div>
</section>

<section class="about">
  <div class="abs about-mark"><span>Marguerite Halloway Associates</span></div>
  <p class="abs about-tagline">EMPOWERING CREATIVITY</p>
  <p class="abs about-kicker">About Me</p>
  <h2 class="abs about-name">Marguerite Halloway</h2>
  <p class="abs about-copy">Lorem ipsum dolor sit amet consectetur. Sit pellentesque ut eu et<br>id praesent quam. Purus at amet sed tempor. Cras in augue amet<br>facilisi id ornare ultrices in. Consequat in accumsan ut ullamcorper.<br>Diam facilisis fringilla leo parturient ac purus leo massa faucibus.<br>Tincidunt praesent sollicitudin luctus id nec netus. Libero turpis sit<br>malesuada purus non sed. Elementum mauris lacus eget viverra in<br>amet lectus lacus varius. Vel viverra imperdiet egestas tellus urna.<br>Lacus interdum platea magna posuere. Diam gravida mauris enim<br>semper scelerisque bibendum libero.</p>
  <a class="btn" href="#" style="left:602px;top:1154px;width:154px;height:46px">LET'S MEET</a>
</section>

<section class="services">
  <p class="abs center" style="top:46px;font-size:17px">Our Services</p>
  <h2 class="abs center" style="top:82px;font-size:31px;font-weight:500;line-height:37px">Lorem ipsum dolor sit amet<br>consectetur. Amet ornare.</h2>

  <div class="abs service-photo" style="left:248px;top:205px" role="img" aria-label="Photo of a woman at a desk with a chart on a monitor"></div>
  <h3 class="abs service-title" style="left:262px;top:354px">Service 1</h3>
  <p class="abs service-copy" style="left:262px;top:390px">Lorem ipsum dolor sit amet consectetur. Quis risus eu magnis sodales.</p>

  <div class="abs service-photo" style="left:516px;top:205px" role="img" aria-label="Photo of a woman at a desk with a chart on a monitor"></div>
  <h3 class="abs service-title" style="left:531px;top:354px">Service 1</h3>
  <p class="abs service-copy" style="left:531px;top:390px">Lorem ipsum dolor sit amet consectetur. Quis risus eu magnis sodales.</p>

  <div class="abs service-photo" style="left:770px;top:216px" role="img" aria-label="Photo of a woman at a desk with a chart on a monitor"></div>
  <h3 class="abs service-title" style="left:785px;top:364px">Service 1</h3>
  <p class="abs service-copy" style="left:785px;top:400px">Lorem ipsum dolor sit amet consectetur. Quis risus eu magnis sodales.</p>
</section>

<section class="events">
  <h2 class="abs center" style="top:1897px;font-size:27px;font-weight:600">Event</h2>

  <div class="abs event-photo event-one" style="left:164px;top:1964px" role="img" aria-label="Illustration of women working creatively"><span class="event-date">15 January 2023</span></div>
  <h3 class="abs event-title" style="left:164px;top:2164px">Lorem ipsum dolor sit</h3>
  <p class="abs event-copy" style="left:164px;top:2195px">Lorem ipsum dolor sit amet consectetur. Quis risus eu magnis sodales.</p>
  <a class="btn" href="#" style="left:164px;top:2275px;width:154px;height:46px">More Details <svg width="14" height="12" viewBox="0 0 14 12" fill="none" stroke="#fff" stroke-width="1.5"><path d="M1 6h12M8 1l5 5-5 5"/></svg></a>

  <div class="abs event-photo event-two" style="left:461px;top:1964px" role="img" aria-label="Illustration of a diverse crowd of women"><span class="event-date" style="left:16px;bottom:32px">16 January 2023</span></div>
  <h3 class="abs event-title" style="left:461px;top:2164px">Lorem ipsum dolor sit</h3>
  <p class="abs event-copy" style="left:461px;top:2195px">Lorem ipsum dolor sit amet consectetur. Quis risus eu magnis sodales.</p>
  <a class="btn" href="#" style="left:461px;top:2275px;width:154px;height:46px">More Details <svg width="14" height="12" viewBox="0 0 14 12" fill="none" stroke="#fff" stroke-width="1.5"><path d="M1 6h12M8 1l5 5-5 5"/></svg></a>

  <div class="abs event-photo event-three" style="left:770px;top:1964px" role="img" aria-label="Poster artwork for a women in leadership event"><span class="event-date" style="left:8px;bottom:32px">20 January 2023</span></div>
  <h3 class="abs event-title" style="left:760px;top:2164px">Lorem ipsum dolor sit</h3>
  <p class="abs event-copy" style="left:760px;top:2195px">Lorem ipsum dolor sit amet consectetur. Quis risus eu magnis sodales.</p>
  <a class="btn" href="#" style="left:760px;top:2275px;width:154px;height:46px">More Details <svg width="14" height="12" viewBox="0 0 14 12" fill="none" stroke="#fff" stroke-width="1.5"><path d="M1 6h12M8 1l5 5-5 5"/></svg></a>
</section>

<section class="contact">
  <h2 class="abs center" style="top:46px;font-size:31px;font-weight:500">Contact Us</h2>

  <div class="abs contact-item" style="top:154px">
    <svg width="40" height="40" viewBox="0 0 40 40" fill="none" stroke="#1a1a1a" stroke-width="1.3"><circle cx="20" cy="20" r="19"/><path d="M20 29s-7-7-7-12a7 7 0 0 1 14 0c0 5-7 12-7 12z"/><circle cx="20" cy="17" r="2.5"/></svg>
    <p>Location<br>Lorem ipsum dolor sit<br>amet consectetur. Sit.</p>
  </div>
  <div class="abs contact-item" style="top:249px">
    <svg width="40" height="40" viewBox="0 0 40 40" fill="none" stroke="#1a1a1a" stroke-width="1.3"><circle cx="20" cy="20" r="19"/><path d="M20 29s-7-7-7-12a7 7 0 0 1 14 0c0 5-7 12-7 12z"/><circle cx="20" cy="17" r="2.5"/></svg>
    <p>Phone<br>+888 8888 888</p>
  </div>
  <div class="abs contact-item" style="top:331px">
    <svg width="40" height="40" viewBox="0 0 40 40" fill="none" stroke="#1a1a1a" stroke-width="1.3"><circle cx="20" cy="20" r="19"/><path d="M20 29s-7-7-7-12a7 7 0 0 1 14 0c0 5-7 12-7 12z"/><circle cx="20" cy="17" r="2.5"/></svg>
    <p>Email<br>info@margueritehallowayassociates.example</p>
  </div>

  <div class="field" style="top:132px;height:48px">Name</div>
  <div class="field" style="top:199px;height:47px">Phone</div>
  <div class="field" style="top:269px;height:47px">Email</div>
  <div class="field" style="top:330px;height:93px">Message</div>
  <a class="btn" href="#" style="left:585px;top:445px;width:154px;height:45px">SUMBIT</a>
</section>

<footer class="site-footer">
  <nav class="footer-links">
    <a href="#" style="left:421px">Terms &amp;Conditions</a>
    <a href="#" style="left:599px">Privacy Policy</a>
    <a href="#" style="left:752px">About</a>
  </nav>
  <p class="abs center" style="top:112px;font-size:13.6px">Copyrights 2023 Marguerite Halloway Associates All Rights Reserved</p>
  <div class="abs socials">
    <span><i></i>Facelink</span>
    <span><i></i>Pictagram</span>
    <span><i></i>WorkNet</span>
  </div>
</footer>

</body>
</html>
```